ALL TYPES OF COMMERCIAL PLASTERING

TYPE OF BLOCK LETTERING WITH STAND OUT QUALITIES
WITH SOME TYPE OF LOGO
SOMETHING UNIQUE FOR THE BUILDING INDUSTRY.
QUALITY WORKMANSHIP
Updates

forgot to include my mobile phone number on my brief. could you add it to your design please MOBILE PH 0412 858 196

please let me make this quite clear ,the company name is harbourline linings and Fitouts PTY LTD. THE TYPE OF WORK WE WILL BE DOING IS COMMERCIAL PLASTERING.

Industry/Entity Type

Industry

Contact Information for Business Card

harbourline linings and fitouts P/L
marcus devlin p.o.box 42 wendouree 3355 email address harbourlinelinings@examplemail.com
ABN 51 718 294 605 COMMERCIAL PLASTERING

```html
<!DOCTYPE html>
<html lang="en">
<head>
<meta charset="utf-8">
<title>Harbourline Linings and Fitouts P/L – Business Card</title>
<link href="https://fonts.googleapis.com/css2?family=Cinzel:wght@700&family=Arimo:wght@400&display=swap" rel="stylesheet">
<style>
  :root {
    --orange: #f28c00;
    --black: #0d0d0d;
    --white: #ffffff;
    --backdrop: #e9e6e1;
    --ink: #1a1a1a;
  }
  html, body {
    margin: 0;
    width: 1200px;
    height: 800px;
    overflow: hidden;
    background: var(--backdrop);
  }
  .card {
    position: absolute;
    left: 75px;
    top: 100px;
    width: 1050px;
    height: 600px;
    background: var(--white);
    overflow: hidden;
    box-shadow: 0 10px 30px rgba(0,0,0,0.18);
    font-family: "Arimo", Arial, sans-serif;
  }
  .card-waves {
    position: absolute;
    inset: 0;
  }
  .brand {
    position: absolute;
    left: 60px;
    top: 42px;
    display: flex;
    align-items: flex-start;
    gap: 26px;
  }
  .brand-dot {
    width: 120px;
    height: 120px;
    border-radius: 50%;
    background: var(--orange);
    flex: none;
  }
  .brand-text { padding-top: 10px; }
  .brand-name {
    font-family: "Cinzel", "Times New Roman", serif;
    font-weight: 700;
    color: var(--orange);
    font-size: 46px;
    line-height: 1.02;
    letter-spacing: 1px;
    margin: 0;
    text-transform: uppercase;
  }
  .brand-name .line-two { display: block; padding-left: 10px; }
  .brand-tagline {
    margin: 10px 0 0 4px;
    font-size: 22px;
    color: var(--ink);
    letter-spacing: 0.5px;
  }
  .contact {
    position: absolute;
    left: 80px;
    top: 250px;
    margin: 0;
    padding: 0;
    list-style: none;
  }
  .contact li {
    display: flex;
    align-items: center;
    gap: 28px;
    font-size: 27px;
    color: var(--ink);
    height: 44px;
  }
  .contact svg { width: 26px; height: 26px; fill: var(--orange); flex: none; }
  .person {
    position: absolute;
    left: 640px;
    top: 395px;
  }
  .person-name {
    margin: 0;
    font-size: 38px;
    color: var(--orange);
    font-weight: 400;
  }
  .person-phone {
    margin: 6px 0 0;
    font-size: 27px;
    color: var(--ink);
  }
</style>
</head>
<body>
  <div class="card">
    <svg class="card-waves" viewBox="0 0 1050 600" aria-hidden="true">
      <path d="M0 385 C 210 420, 420 565, 700 585 C 850 595, 960 585, 1050 575 L1050 600 L0 600 Z" fill="var(--black)"/>
      <path d="M0 355 C 220 390, 430 535, 700 560 C 850 572, 960 566, 1050 556" fill="none" stroke="var(--orange)" stroke-width="9"/>
    </svg>

    <div class="brand">
      <div class="brand-dot"></div>
      <div class="brand-text">
        <h1 class="brand-name">Harbourline Linings<span class="line-two">and Fitouts P/L</span></h1>
        <p class="brand-tagline">COMMERCIAL PLASTERING</p>
      </div>
    </div>

    <ul class="contact">
      <li>
        <svg viewBox="0 0 24 24"><path d="M12 2a7 7 0 0 0-7 7c0 5 7 13 7 13s7-8 7-13a7 7 0 0 0-7-7zm0 9.5a2.5 2.5 0 1 1 0-5 2.5 2.5 0 0 1 0 5z"/></svg>
        ABN 51 718 294 605
      </li>
      <li>
        <svg viewBox="0 0 24 24"><path d="M12 3 2 12h3v9h5v-6h4v6h5v-9h3z"/></svg>
        p.o.box 42 wendouree 3355
      </li>
      <li>
        <svg viewBox="0 0 24 24"><path d="M2 5h20v14H2z" /><path d="M2 5l10 8 10-8" fill="none" stroke="#fff" stroke-width="1.8"/></svg>
        harbourlinelinings@examplemail.com
      </li>
    </ul>

    <div class="person">
      <p class="person-name">marcus devlin</p>
      <p class="person-phone">0412 858 196</p>
    </div>
  </div>
</body>
</html>
```